Web Design for Solar Energy Consultancy Company

~ May 3, 2017 Update ~
As our project is rapidly progressing towards its completion, we started building up the list of designs that attracted the most of the team's attention. Additional submittals are still most welcome. Before submitting your proposal, however, we can recommend to review the concepts that received 4 stars as these are the ones that, in our opinion, most closely match the brief's requirements. Thank you!!
~ April 30, 2017 Update ~
The project deadline has been extended to attract a broader design community and to better tailor the final design to the requirements of the project.
A "light", "clean" (minimalistic), professionally looking, unique design is expected. Please, try to avoid industry cliches. Also, please use green, which became another industry cliche, with great caution. The brief provides minimum details to foster creativity. With the same notion in mind, the page content information is not provided.
Thank you for your feedback and support of the project!!
~ April 22, 2017 Update ~
Additional comments after starting receiving more designs:
- your attention to the brief's requirements will be highly appreciated. It is expected that the design is unique - standard, commonly used, images, formats and approaches do not fall under this category. There is no need to "bombard" with slightly different variations of the same design. It is expected that a conceptual (preliminary) design is submitted first, and, after it is reviewed (each design will receive a star rating and, if the star rating is greater than 3, a detailed feedback), the requested changes are implemented. We believe this will allow to approach the design process more efficiently and safe additional time to both the Designers's Community and our company. Thank you for understanding.
Clarification, please submit two variations of a design:
1) 1 page "business card" design that the company will be able to use during its startup stage;
2) the fully functional design (as per the requirements outlined below) for the company to transition to after the start-up period is over. Same design principles as developed for option 1 should be used for this variation.
Additional clarification, please note that the news block will not require images (at least during the start-up stage). It is envisioned to be a news feeder.
~ April 21, 2017 Update ~
Preliminary comments after receiving first designs:
- please try to create a unique design, using common elements wisely. Though such solar energy "attributes" as a solar panel or a bulb are very well recognized and allow quickly identify the nature of the business, they also became so common that in many cases a design may seem very similar to the one of others (Oh!, I've already seen this... effect).
- please try to introduce the company's logo unobtrusively. The size and position of the logo should clearly identify the company, but the message should be subtle, the logo should not distract from the main design. Brevam's swoosh did not need to occupy have the screen.
- please use the green color with caution as it was with the company's logo. True, it is a green energy. But there is no need for the color to "scream" about it. Use the amount of green and its tone (avoid acid green) wisely.
--------------------------------------------------------------------------------
1. Main Goal
Develop a website that can represent the company to the industry stakeholders and become its "business card" during the start-up stage.
2. Secondary Goal
Develop a structure of a fully functional website that the "business card" design can eventually be transformed to staying consistent with the original design principles.
3. Key Audience
Varlo Corp. is providing consulting and technical services in the area of Solar Energy. The industry stakeholders include project developers, financial community, governmental bodies, OEMs, and competition.
4. Site Map
- HOME
• About
• Services
• Solar Energy
• News
• Contacts
• Social Media
- SERVICES*
- PROJECTS*
- FINANCE*
- TRAINING*
- SOLAR (ENERGY)*
* Maybe inactive / partially functional during the start-up stage.
5. Technical Specifications
Online brochure website during the start-up stage with a capability to be eventually transformed to a fully functional website while preserving the original design principles.
The design to be appealing, "light", professional, and with an intuitive and easy to navigate interface. Modern coding principles supporting efficiency and security to be utilized. Newest industry trends in website coding will be welcome.
The website to be designed so that it would fit well a computer, tablet, or mobile phone screen of any size. Cross-platform functionality to be taken into consideration to ensure that the website is fully functional on any platform.
Company's logo has already been designed and will be shared with the short-listed designers during the final design stage.
6. Interaction
The website will provide information about the company, our services, and projects. In addition, the industry insight, accumulated knowledge, and most recent trends are planned to be shared with stakeholders and attract and retain the audience.
Interaction with designers during the website development is envisioned to go through the following steps:
a) conceptual design - to be proposed by a designer originally. All conceptual designs will be reviewed and a feedback provided to pre-selected designers;
b) (preliminary and) final design - depending on the level of additional changes required can be broken into two steps. After discussing preliminary designs, company images will be provided to the selected finalists, who will compete with their final proposals.
7. Industry Stakeholders
- https://www.quelbrant.example/power/solar-power.- http://www.tavlorpeak.example/
- http://www.morvexaworks.example/about/company/
- https://www.pyxbel.example/energy/index.html
8. Budget
Defined by the project.
9. Timescale
Defined by the project.
12. Additional Info
- No copy-cats, standard graphics, or cliches please!
- Additional information / clarifications will be gladly provided upon request.
- This specification may be updated throughout the project to reflect discussions with / changes proposed by the Designers community.
Updates

```html
<!DOCTYPE html>
<html lang="en">
<head>
<meta charset="utf-8">
<title>Varlo Corp. — Solar Energy Consultancy</title>
<link href="https://fonts.googleapis.com/css2?family=Michroma&family=Open+Sans:ital,wght@0,400;0,600;0,700;1,400&display=swap" rel="stylesheet">
<style>
:root{
  --accent:#f0a01e;
  --dark:#55443b;
  --darker:#3e322c;
  --mid:#7d6c60;
  --sand:#efe4d7;
  --ink:#2a2320;
  --muted:#7a726c;
  --white:#ffffff;
  --line:#d9d3cc;
}
*{box-sizing:border-box;margin:0;padding:0}
html,body{width:1200px;height:2368px;overflow:hidden}
body{position:relative;font-family:"Open Sans",Arial,sans-serif;color:var(--ink);background:var(--white)}
.abs{position:absolute}
.title{font-family:"Michroma","Open Sans",sans-serif;font-weight:400;letter-spacing:1px}
.rule{display:block;width:16px;height:2px;background:var(--accent)}

/* header */
.site-header{left:0;top:0;width:1200px;height:60px;background:rgba(245,242,238,.96);z-index:2}
.brand{left:176px;top:14px;display:flex;align-items:center;gap:8px}
.brand-dot{width:30px;height:30px;border-radius:50%;background:var(--accent)}
.brand-name{font-size:20px;font-weight:700;color:var(--ink);letter-spacing:1px}
.main-nav{right:172px;top:36px;display:flex;gap:20px;font-size:12.5px}
.main-nav a{color:var(--ink);text-decoration:none;padding-bottom:6px}
.main-nav a.active{border-bottom:2px solid var(--muted)}
.social{display:flex;gap:6px}
.social span{display:block;width:21px;height:21px;border:1px solid currentColor}
.header-social{right:183px;top:9px;color:var(--ink)}

/* hero */
.hero{left:0;top:60px;width:1200px;height:417px;background:linear-gradient(180deg,#c9a889 0%,#e9b57a 22%,#8a7148 40%,#5b5a34 60%,#6e5a4a 100%)}
.hero-caption{left:630px;top:247px;width:395px;height:96px;background:rgba(255,255,255,.42);padding:24px 26px}
.hero-caption h1{font-size:20px;color:var(--ink);margin-bottom:6px}
.hero-caption p{font-size:14px;color:var(--ink)}

/* about / services */
.band-edge{left:0;top:477px;width:132px;height:326px;background:var(--dark)}
.about-panel{left:132px;top:477px;width:467px;height:326px;background:var(--mid);color:var(--white);text-align:center}
.about-panel h2{font-family:"Open Sans",sans-serif;font-weight:700;font-size:13px;letter-spacing:1px;margin-top:108px}
.about-panel .rule{margin:24px auto 0}
.about-panel p{font-size:12.5px;line-height:19px;width:300px;margin:26px auto 0}
.dots{display:flex;gap:8px;justify-content:center;align-items:center}
.dots i{display:block;width:5px;height:5px;border-radius:50%;background:currentColor}
.dots i.on{width:9px;height:9px;background:none;border:1.5px solid currentColor}
.about-panel .dots{margin-top:46px}
.services-panel{left:599px;top:477px;width:601px;height:326px;background:var(--sand);padding:60px 34px}
.notch{width:0;height:0;border-top:12px solid transparent;border-bottom:12px solid transparent;border-left:12px solid var(--mid)}
.services-panel h2{font-size:12px;margin-bottom:10px}
.services-panel p{font-size:12.5px;line-height:22px;margin-top:22px;width:380px}
.btn{display:inline-block;border:2px solid var(--ink);font-weight:700;font-size:12px;padding:6px 16px;color:var(--ink)}
.services-panel .btn{margin-top:52px}

/* we provide */
.provide-title{left:178px;top:873px}
.provide-title h2{font-size:16px;margin-bottom:12px}
.provide-intro{left:468px;top:873px;width:560px;font-size:12.5px;line-height:23px;color:var(--muted)}
.offer{top:962px;width:260px}
.offer svg{display:block}
.offer h3{font-family:"Michroma",sans-serif;font-size:12px;font-weight:400;margin-top:18px}
.offer .gray{display:block;width:20px;height:1px;background:var(--line);margin:10px 0 10px}
.offer p{font-size:12.5px;line-height:19px;color:var(--muted)}
.more{display:inline-flex;align-items:center;gap:6px;font-size:10.5px;font-weight:700;color:var(--accent);margin-top:28px}

/* projects band */
.projects-panel{left:0;top:1233px;width:380px;height:418px;background:var(--dark);color:var(--white)}
.projects-panel h2{position:absolute;left:178px;top:72px;font-size:16px;letter-spacing:4px}
.projects-panel .rule{position:absolute;left:178px;top:102px}
.proj-name{position:absolute;right:55px;top:148px;font-family:"Michroma",sans-serif;font-size:11px}
.proj-sub{position:absolute;right:55px;top:172px;font-size:11px}
.arrows{position:absolute;left:246px;top:238px;display:flex;gap:4px}
.arrows span{width:36px;height:34px;background:var(--mid);display:flex;align-items:center;justify-content:center}
.projects-panel .btn{position:absolute;left:206px;top:319px;border-color:var(--white);color:var(--white);border-width:1px;padding:8px 12px}
.project-photo{left:380px;top:1233px;width:292px;height:418px;background:linear-gradient(180deg,#f5c75a 0%,#f5a93a 45%,#e0642a 75%,#4a2418 100%)}
.solar-panel{left:672px;top:1233px;width:528px;height:418px;background:var(--sand);padding:0 40px 0 24px}
.solar-panel .notch{position:absolute;left:-12px;top:22px;border-left:none;border-right:12px solid var(--sand)}
.solar-panel h2{font-size:16px;letter-spacing:4px;margin-top:72px}
.solar-lead{font-style:italic;font-size:12.5px;line-height:22px;margin-top:28px}
.solar-body{font-size:12.5px;line-height:22px;color:var(--muted);margin-top:22px}

/* news */
.news-title{left:178px;top:1710px;display:flex;align-items:center}
.news-title h2{font-size:16px;letter-spacing:4px}
.news-line{left:416px;top:1720px;width:608px;height:1px;background:var(--line)}
.news-rule{left:178px;top:1744px}
.card{top:1786px;width:272px;height:229px;background:var(--sand)}
.date{position:absolute;left:0;top:0;width:66px;height:66px;background:var(--mid);color:var(--white);text-align:center}
.date b{display:block;font-family:"Michroma",sans-serif;font-weight:400;font-size:26px;line-height:46px}
.date span{display:block;background:var(--darker);font-size:13px;font-weight:700;line-height:20px}
.card h3{position:absolute;left:72px;top:15px;width:190px;font-family:"Michroma",sans-serif;font-weight:400;font-size:10.5px;line-height:18px}
.card p{position:absolute;left:16px;top:86px;width:240px;font-size:11px;line-height:18.5px;color:var(--muted)}
.card .more{position:absolute;left:16px;top:192px;margin:0}
.news-dots{left:0;top:2052px;width:1200px;color:var(--ink)}

/* footer */
.site-footer{left:0;top:2105px;width:1200px;height:263px;background:var(--darker);color:#a49a92;font-size:11px}
.to-top{left:588px;top:2096px;width:24px;height:14px}
.news-label{position:absolute;left:180px;top:81px;font-family:"Michroma",sans-serif;font-size:12px;color:#c8bfb7}
.mail{position:absolute;left:182px;top:117px;width:176px;border-bottom:1px solid #6b5d55;padding-bottom:6px;font-style:italic;color:#a49a92;font-size:12px}
.contact{position:absolute;left:402px;display:flex;gap:14px}
.contact svg{flex:none;margin-top:2px}
.f-links{position:absolute;top:82px;line-height:21px}
.footer-social{position:absolute;left:834px;top:117px;color:#a49a92}
.footer-social span{width:23px;height:23px}
.copy{position:absolute;right:180px;top:234px;font-size:10px}
</style>
</head>
<body>

<header class="site-header abs">
  <div class="brand abs"><span class="brand-dot"></span><span class="brand-name">VARLO</span></div>
  <nav class="main-nav abs">
    <a class="active">Home</a><a>About</a><a>Services</a><a>Projects</a><a>Finance</a><a>Training</a><a>Solar Energy</a><a>News</a><a>Contact us</a>
  </nav>
  <div class="social header-social abs" aria-label="Social links"><span></span><span></span><span></span></div>
</header>

<section class="hero abs" role="img" aria-label="Aerial view of a solar farm beside a river at sunset"></section>
<div class="hero-caption abs">
  <h1 class="title">SHOULDER RESPONSIBILITY</h1>
  <p>Join hands with us to better your living</p>
</div>

<div class="band-edge abs"></div>
<section class="about-panel abs">
  <svg class="abs" style="left:218px;top:48px" width="30" height="40" viewBox="0 0 30 40" fill="none" stroke="#fff" stroke-width="1.4">
    <path d="M15 2a11 11 0 0 0-6 20v5h12v-5a11 11 0 0 0-6-20z"/><path d="M10 31h10M11 35h8M13 22v-6l2 2 2-2v6"/>
  </svg>
  <h2>ABOUT</h2>
  <span class="rule"></span>
  <p>Duis aute irure dolor in reprehenderit in volupt ate velit esse cillum dolore eu fugiat nulla tutur Excepteur sint occaec.</p>
  <div class="dots"><i></i><i class="on"></i><i></i></div>
</section>
<section class="services-panel abs">
  <div class="notch abs" style="left:0;top:46px"></div>
  <h2 class="title">SERVICES</h2>
  <span class="rule"></span>
  <p>Lorem ipsum dolor sit amet, consectetur adipiscing elit, sed do eiusmod tempor incididunt ut labore et dolore magna aliqua. Ut enim ad minim veniam, quis nostrud.</p>
  <span class="btn">MORE</span>
</section>

<div class="provide-title abs"><h2 class="title">WE PROVIDE</h2><span class="rule"></span></div>
<p class="provide-intro abs">Lorem ipsum dolor sit amet, consectetur adipiscing elit, sed do eiusmod tempor incididunt ut labore et dolore magna aliqua. Ut enim ad minim veniam.</p>

<article class="offer abs" style="left:178px">
  <svg width="32" height="30" viewBox="0 0 32 30" fill="none" stroke="#55443b" stroke-width="1.3"><rect x="5" y="2" width="25" height="18"/><path d="M2 7v18l5-4h16"/><path d="M10 8h15M10 12h15M10 16h9"/></svg>
  <h3>Advisory</h3><span class="gray"></span>
  <p>Excepteur sint occaecat cupida tat non ed proident, sunt in culpa qui officia deserunt mollit onsectetuer adipiscing elit</p>
  <span class="more">MORE <svg width="12" height="8" viewBox="0 0 12 8"><path d="M0 4h10M7 1l3 3-3 3" stroke="#f0a01e" fill="none" stroke-width="1.5"/></svg></span>
</article>
<article class="offer abs" style="left:472px">
  <svg width="28" height="30" viewBox="0 0 28 30" fill="none" stroke="#55443b" stroke-width="1.3"><circle cx="14" cy="18" r="10"/><path d="M11 8l3-5 3 5M6 26l-2 3M22 26l2 3"/><circle cx="9" cy="16" r="1"/></svg>
  <h3>Finance</h3><span class="gray"></span>
  <p>Quis nostrum exercitationem ullam corp oris suscipit labor iosam, nisi ut aliquid ex quis nostrud exerci tation ullam</p>
  <span class="more">MORE <svg width="12" height="8" viewBox="0 0 12 8"><path d="M0 4h10M7 1l3 3-3 3" stroke="#f0a01e" fill="none" stroke-width="1.5"/></svg></span>
</article>
<article class="offer abs" style="left:763px">
  <svg width="32" height="30" viewBox="0 0 32 30" fill="none" stroke="#55443b" stroke-width="1.3"><rect x="2" y="3" width="28" height="18"/><path d="M16 21v4M10 29l6-4 6 4M11 16v-4M15 16v-7M19 16v-5"/></svg>
  <h3>Training</h3><span class="gray"></span>
  <p>At vero eos et accusamus et iusto odio dignissimos ducimu srtui blanditiis praese Duis autem vel eum iriure dolor</p>
  <span class="more">MORE <svg width="12" height="8" viewBox="0 0 12 8"><path d="M0 4h10M7 1l3 3-3 3" stroke="#f0a01e" fill="none" stroke-width="1.5"/></svg></span>
</article>

<section class="projects-panel abs">
  <h2 class="title">PROJECTS</h2>
  <span class="rule"></span>
  <div class="proj-name">QUAE VOLUPTATEM</div>
  <div class="proj-sub">Analytical Solar Counseling</div>
  <div class="arrows">
    <span><svg width="8" height="12" viewBox="0 0 8 12"><path d="M6 1L1 6l5 5" stroke="#fff" fill="none" stroke-width="1.5"/></svg></span>
    <span><svg width="8" height="12" viewBox="0 0 8 12"><path d="M2 1l5 5-5 5" stroke="#fff" fill="none" stroke-width="1.5"/></svg></span>
  </div>
  <span class="btn">VIEW PROJECTS</span>
</section>
<div class="project-photo abs" role="img" aria-label="Street lamps silhouetted against a setting sun"></div>
<section class="solar-panel abs">
  <div class="notch"></div>
  <h2 class="title">SOLAR ENERGY</h2>
  <p class="solar-lead">Sed ut perspiciatis unde omnis iste natus error sit volu ptatem accusantium dolor em que laudantium, totam rem aperiam, eaque ipsa quae ab. consectetuer adipis cing elit, sed diam nonummy nibh euismod.</p>
  <p class="solar-body">Quis autem vel eum iure reprehenderit qui in ea volu ptate velit esse quam nihil molestiae consequatur. dolorem ipsum quia dolor sit amet consectetur. twisi enim ad minim veniam, quis nostrud exerci tation ullamcorper suscipit lobortis nisl ut aliquip ex ea commodo consequat.</p>
</section>

<div class="news-title abs"><h2 class="title">LATEST NEWS</h2></div>
<div class="news-line abs"></div>
<span class="rule news-rule abs"></span>

<article class="card abs" style="left:170px">
  <div class="date"><b>15</b><span>Apr</span></div>
  <h3>Esse molestie consequat, vel illum dolore eu feugiat nulla facilisis</h3>
  <p>Lit esse quam nihil molestiae consequ atur, dolorem ipsum quia dolor sit amet consec tetur. twisi enim ad minim vel iam, quis nost rud exerci tation ullamco rper suscipit lobo rtis ni</p>
  <span class="more">MORE <svg width="12" height="8" viewBox="0 0 12 8"><path d="M0 4h10M7 1l3 3-3 3" stroke="#f0a01e" fill="none" stroke-width="1.5"/></svg></span>
</article>
<article class="card abs" style="left:463px">
  <div class="date"><b>29</b><span>Mar</span></div>
  <h3>Lorem ipsum dolor sit amet, consectetuer adipiscing elit sed diam nonummy</h3>
  <p>Qwisi enim ad minim ven iam,lit esse quam nihil molestiae consequ atur. dolorem ipsum quia dolor sit amet consec tetur. Quis nost rud exerci tation ullamco rper suscipit lobo rtis ni</p>
  <span class="more">MORE <svg width="12" height="8" viewBox="0 0 12 8"><path d="M0 4h10M7 1l3 3-3 3" stroke="#f0a01e" fill="none" stroke-width="1.5"/></svg></span>
</article>
<article class="card abs" style="left:755px">
  <div class="date"><b>17</b><span>Mar</span></div>
  <h3>Esse molestie consequat, vel illum dolore eu feugiat nulla facilisis</h3>
  <p>lit esse quam nihil molestiae consequ atur, dolorem ipsum quia dolor sit amet consec tetur. twisi enim ad minim vel iam, quis nost rud exerci tation ullamco rper suscipit lobo rtis ni</p>
  <span class="more">MORE <svg width="12" height="8" viewBox="0 0 12 8"><path d="M0 4h10M7 1l3 3-3 3" stroke="#f0a01e" fill="none" stroke-width="1.5"/></svg></span>
</article>

<div class="dots news-dots abs"><i></i><i class="on"></i><i></i></div>

<footer class="site-footer abs">
  <div class="news-label">FOR NEWSLETTER</div>
  <div class="mail">Enter mail id...
    <svg class="abs" style="right:0;top:2px" width="12" height="12" viewBox="0 0 12 12"><path d="M0 6L12 0 8 12 6 7z" fill="#f0a01e"/></svg>
  </div>
  <div class="contact" style="top:80px">
    <svg width="10" height="12" viewBox="0 0 10 12"><path d="M5 0a4 4 0 0 0-4 4c0 3 4 8 4 8s4-5 4-8a4 4 0 0 0-4-4z" fill="#a49a92"/><circle cx="5" cy="4" r="1.5" fill="#3e322c"/></svg>
    <span style="line-height:16px">27 Harlow Street, 4th Floor,<br>Brenton, MA 02190</span>
  </div>
  <div class="contact" style="top:125px">
    <svg width="10" height="12" viewBox="0 0 10 12"><path d="M2 0l2 3-1 2c1 2 2 3 4 4l1-1 2 2-2 2C4 12 0 6 0 2z" fill="#a49a92"/></svg>
    <span>(555) 014-2290</span>
  </div>
  <div class="contact" style="top:160px">
    <svg width="12" height="10" viewBox="0 0 12 10"><rect width="12" height="9" fill="#a49a92"/><path d="M0 0l6 5 6-5" stroke="#3e322c" fill="none"/></svg>
    <span>info@varlocorp.example</span>
  </div>
  <div class="f-links" style="left:628px">Home<br>About<br>Services<br>Projects</div>
  <div class="f-links" style="left:720px">Finance<br>Solar Energy<br>Training<br>Contacts</div>
  <div class="social footer-social" aria-label="Social links"><span></span><span></span><span></span></div>
  <div class="copy">Copyright © Varlo Corp. 2017</div>
</footer>
<svg class="to-top abs" viewBox="0 0 24 14"><path d="M0 14L12 0l12 14z" fill="#3e322c"/><path d="M8 10l4-4 4 4" stroke="#a49a92" fill="none" stroke-width="1.2"/></svg>

</body>
</html>
```